Business card design needed

would like the title calloway property services to itself be a logo which would also be suitable to use on my van signwriting so needs to be bold and stand out (easily read from a distance)
Target Market(s)
real estate agents, property owners/investors,insurance assessors,
Industry/Entity Type
Business
Contact Information for Business Card
calloway property services
for all your property maintenance and repair needs
-domestic and commercial -rental properties
-insurance repairs -project managment
fully insured/white card
experieced and reliable
ph. ted calloway 0412958364 email teddo7342@quokkamail.net.au
on reverse side of card i would like a list of sevices available
plaster repairs
painting
welding reairs and fabrication
concreting
fencing
minor renovations
pressure cleaning
graffitti removal
rubbish removal
fire restorations
floods
and more no job too big or small
Logo Text
Logo styles of interest
Wordmark Logo
Look and feel

```html
<!DOCTYPE html>
<html lang="en">
<head>
<meta charset="utf-8">
<title>Calloway Property Services – Business Cards</title>
<link rel="stylesheet" href="https://fonts.googleapis.com/css2?family=Open+Sans:ital,wght@0,400;0,600;0,700;0,800;1,400;1,600;1,700&display=swap">
<style>
  :root {
    --bg: #e9e6e3;
    --card: #ffffff;
    --red: #d0161f;
    --red-dark: #a80f16;
    --ink: #111111;
    --muted: #333333;
  }
  * { box-sizing: border-box; margin: 0; padding: 0; }
  html, body { width: 1200px; height: 867px; overflow: hidden; }
  body {
    background: var(--bg);
    font-family: "Open Sans", Arial, sans-serif;
    color: var(--ink);
    position: relative;
  }
  .card {
    position: absolute;
    top: 283px;
    width: 540px;
    height: 300px;
    background: var(--card);
    border-radius: 14px;
    overflow: hidden;
    box-shadow: 0 10px 28px rgba(0,0,0,0.22);
  }
  .card--back { left: 40px; }
  .card--front { left: 620px; }

  /* Back: services list */
  .services {
    position: absolute;
    left: 34px;
    top: 26px;
    width: 200px;
    list-style: none;
  }
  .services li {
    display: flex;
    align-items: center;
    gap: 8px;
    color: var(--red);
    font-style: italic;
    font-size: 15px;
    line-height: 20.5px;
  }
  .services svg { width: 13px; height: 13px; flex: none; }
  .services-more {
    position: absolute;
    left: 34px;
    top: 248px;
    width: 210px;
    text-align: center;
    font-style: italic;
    font-size: 14px;
    line-height: 18px;
    color: var(--ink);
  }
  .services-more strong { font-weight: 700; }
  .divider {
    position: absolute;
    left: 262px;
    top: 34px;
    width: 3px;
    height: 240px;
    background: var(--red);
  }
  .back-details {
    position: absolute;
    left: 286px;
    top: 30px;
    right: 18px;
  }
  .wordmark {
    font-weight: 800;
    color: var(--ink);
    text-transform: uppercase;
    line-height: 1;
    text-align: center;
  }
  .wordmark .line-sub { display: block; }
  .back-details .wordmark { font-size: 31px; letter-spacing: 1px; }
  .back-details .wordmark .line-sub { font-size: 14px; letter-spacing: 1.5px; margin-bottom: 4px; }
  .person-name {
    margin-top: 40px;
    color: var(--red);
    font-weight: 700;
    font-size: 22px;
    line-height: 1.1;
  }
  .person-role {
    font-weight: 700;
    font-size: 13px;
    margin-top: 2px;
  }
  .contact {
    margin-top: 30px;
    font-style: italic;
    font-size: 14px;
    line-height: 19px;
    color: var(--muted);
  }

  /* Front */
  .front-logo {
    position: absolute;
    left: 0; right: 0;
    top: 62px;
  }
  .front-logo .wordmark { font-size: 58px; letter-spacing: 3px; }
  .front-logo .wordmark .line-sub { font-size: 24px; letter-spacing: 3px; margin-bottom: 8px; }
  .tagline-band {
    position: absolute;
    left: 0; right: 0; bottom: 0;
    height: 78px;
    background: linear-gradient(180deg, var(--red) 0%, var(--red-dark) 100%);
    display: flex;
    align-items: center;
    justify-content: center;
  }
  .tagline {
    color: #ffffff;
    font-style: italic;
    font-weight: 600;
    font-size: 20px;
  }
</style>
</head>
<body>
  <svg width="0" height="0" style="position:absolute" aria-hidden="true">
    <symbol id="tick-box" viewBox="0 0 14 14">
      <rect x="1" y="3" width="10" height="10" fill="none" stroke="#111" stroke-width="1.4"/>
      <path d="M3 7.5 L6 10.5 L13 1.5" fill="none" stroke="#d0161f" stroke-width="2.2" stroke-linecap="round" stroke-linejoin="round"/>
    </symbol>
  </svg>

  <section class="card card--back" aria-label="Business card reverse">
    <ul class="services">
      <li><svg><use href="#tick-box"/></svg>painting</li>
      <li><svg><use href="#tick-box"/></svg>welding</li>
      <li><svg><use href="#tick-box"/></svg>reairs and fabrication</li>
      <li><svg><use href="#tick-box"/></svg>concreting</li>
      <li><svg><use href="#tick-box"/></svg>fencing</li>
      <li><svg><use href="#tick-box"/></svg>minor renovations</li>
      <li><svg><use href="#tick-box"/></svg>pressure cleaning</li>
      <li><svg><use href="#tick-box"/></svg>graffitti removal</li>
      <li><svg><use href="#tick-box"/></svg>rubbish removal</li>
      <li><svg><use href="#tick-box"/></svg>fire restorations floods</li>
    </ul>
    <p class="services-more">and more,<br><strong>no job too big or small</strong></p>
    <div class="divider"></div>
    <div class="back-details">
      <div class="wordmark"><span class="line-sub">Property Services</span>Calloway</div>
      <p class="person-name">Ted Calloway</p>
      <p class="person-role">SEO</p>
      <p class="contact">0412958364<br>teddo7342@quokkamail.net.au</p>
    </div>
  </section>

  <section class="card card--front" aria-label="Business card front">
    <div class="front-logo">
      <div class="wordmark"><span class="line-sub">Property Services</span>Calloway</div>
    </div>
    <div class="tagline-band">
      <p class="tagline">for all your property maintenance and repair needs</p>
    </div>
  </section>
</body>
</html>
```